Saltwater In store poster design

We need a poster design that will be hung in aquarium stores, to advertise that they use our natural saltwater.

Must use logo as well as be bright and colourful. We are trying to communicate that the water is natural (so good for your marine tank) as well as clean and safe, so please consider this in your design.

Must say something along the lines of "We use natural ocean water supplied by Reef Bucket in our store" as well as "you can purchase natural ocean water here"

Open to all design types and suggestions as we will update the brief if we find one specific style that we prefer.

Target Market(s)

Customers who own marine aquariums

Industry/Entity Type

Store

Requirements
Must have
• Reef bucket logo (does not need to have blue background attached, just the oval)

Be eye catching

Have similar phrases to those above

```html
<!DOCTYPE html>
<html lang="en">
<head>
<meta charset="utf-8">
<title>Reef Bucket – In-Store Poster</title>
<link rel="stylesheet" href="https://fonts.googleapis.com/css2?family=Archivo+Black&family=Luckiest+Guy&display=swap">
<style>
  :root {
    --page: #ffffff;
    --ink: #0a0a0a;
    --frame: #6e6e6e;
    --ocean-deep: #06213f;
    --ocean-mid: #12477a;
    --ocean-light: #2b6f96;
    --teal: #0f97a3;
    --headline-top: #ffffff;
    --headline-bottom: #6fc4cf;
    --headline-edge: #0d3b5c;
    --muted: #4d4d4d;
    --brand: #1279c6;
  }
  * { margin: 0; padding: 0; box-sizing: border-box; }
  html, body {
    width: 1200px; height: 900px; overflow: hidden;
    background: var(--page);
  }
  .canvas { position: relative; width: 1200px; height: 900px; }
  .poster {
    position: absolute; left: 305px; top: 37px;
    width: 595px; height: 841px;
    border: 1px solid var(--frame);
    background: var(--page);
    overflow: hidden;
    font-family: "Archivo Black", "Arial Black", sans-serif;
  }
  .lead {
    position: absolute; left: 0; right: 0; top: 14px;
    text-align: center; color: var(--ink);
    font-size: 76px; line-height: 66px; letter-spacing: 0.5px;
  }
  .art { position: absolute; left: 0; top: 0; width: 595px; height: 841px; }
  .headline {
    position: absolute; left: 0; right: 0; top: 208px;
    text-align: center;
    font-family: "Luckiest Guy", "Arial Black", cursive;
    font-size: 112px; line-height: 118px; letter-spacing: 2px;
    background: linear-gradient(180deg, var(--headline-top) 20%, var(--headline-bottom) 95%);
    background-size: 100% 118px;
    -webkit-background-clip: text; background-clip: text;
    color: transparent;
    filter: drop-shadow(0 0 1px #fff) drop-shadow(2px 3px 0 var(--headline-edge));
  }
  .here {
    position: absolute; left: 48px; top: 646px;
    color: var(--ink); font-size: 74px; line-height: 80px;
  }
  .supplier {
    position: absolute; left: 300px; top: 654px; width: 260px;
    text-align: center;
  }
  .supplier-label {
    color: var(--muted); font-size: 31px; line-height: 38px; letter-spacing: 0.5px;
  }
  .brand-name {
    margin-top: 46px;
    color: var(--brand); font-size: 35px; line-height: 38px;
  }
  .brand-tagline {
    color: var(--brand); font-size: 15px; line-height: 18px;
  }
</style>
</head>
<body>
<div class="canvas">
  <div class="poster">
    <svg class="art" viewBox="0 0 595 841" aria-hidden="false">
      <defs>
        <linearGradient id="ocean" x1="0" y1="0" x2="0.3" y2="1">
          <stop offset="0" stop-color="var(--ocean-deep)"/>
          <stop offset="0.5" stop-color="var(--ocean-mid)"/>
          <stop offset="1" stop-color="var(--ocean-light)"/>
        </linearGradient>
      </defs>
      <path role="img" aria-label="Underwater photo of a school of silver fish swimming past a coral reef"
            d="M0,181 H595 V578 H175 V690 L0,498 Z" fill="url(#ocean)"/>
      <path class="accent-band" fill="var(--teal)"
            d="M0,498 L175,690 V578 H595 V618 H250 Q200,618 200,668 V738 Q200,760 183,748 L0,573 Z"/>
    </svg>

    <h1 class="lead">You can<br>purchase</h1>
    <p class="headline">NATURAL<br>OCEAN<br>WATER</p>
    <p class="here">here</p>

    <div class="supplier">
      <p class="supplier-label">supplied by</p>
      <p class="brand-name">Reef Bucket</p>
      <p class="brand-tagline">Saltwater Deliveries</p>
    </div>
  </div>
</div>
</body>
</html>
```